Poster for a Vegetarian Food Truck/Restaurant

Ours is a food truck with lots of greens in the menu. The name of our restaurant is Tidal Crumbs.

I want to create a Poster image for the restaurant. Please submit designs on any one or both the themes described below

Size: 1.6 meters by 4.6 meters (horizontal)

Design Theme #1
A poster based off 'Newspaper front page'.
The poster should look like the front page of a newspaper with 'Tidal Crumbs' as its name. The Tidal Crumbs should appear prominently (in green color, possibly light green or lemon color). The poster will have a few snippets about benefits of certain food items or some trivia along with an image. For example 'Garlic is high in minerals & vitamins', 'Chickpeas are high on fiber'. I'll decide on the exact text meanwhile.

I have attached 2 sample images to give an idea.

Design Theme #2

It should consist of the following 3 components:
1. Green Forest like back ground
2. Image of a chef with a welcoming, smiling face
3. The text 'Tidal Crumbs' should appear in the poster

I want Bram Oakhurst lookalike, the main character from the animation movie 'Windy with a sprinkle of dumplings' to be the chef placed in the poster.
The chef should appear confident, smiling, young with his typical hair style

A sample picture of bram oakhurst is attached in the brief

Target Market(s)

The poster will be pasted on a food truck

Industry/Entity Type

Restaurant

Requirements
Must have
• Poster with light but high resolution image(s)
• Attention to detail
Should not have
• The poster should not have dense/dark colors

```html
<!DOCTYPE html>
<html lang="en">
<head>
<meta charset="utf-8">
<title>Tidal Crumbs — Front Page</title>
<link rel="stylesheet" href="https://fonts.googleapis.com/css2?family=Open+Sans&family=Tinos&family=Carlito&display=swap">
<style>
  :root {
    --green: #39b54a;
    --ink: #111111;
    --paper: #ffffff;
    --rule: #8c8c8c;
    --ad-grey: #87878a;
    --frame: #555555;
  }
  * { margin: 0; padding: 0; box-sizing: border-box; }
  html, body { width: 1200px; height: 417px; overflow: hidden; background: var(--paper); }
  .page {
    position: relative; width: 1200px; height: 417px; overflow: hidden;
    background: var(--paper); color: var(--ink);
    font-family: "Open Sans", Arial, sans-serif;
  }
  .top-rule { position: absolute; left: 0; top: 3px; width: 1200px; height: 3px; background: var(--rule); }
  .dateline { position: absolute; left: 14px; top: 20px; font-size: 14px; line-height: 21px; }
  .dateline .city { margin-top: 7px; }
  .masthead {
    position: absolute; left: 0; top: 16px; width: 1200px; text-align: center;
    font-family: "Tinos", "Times New Roman", serif; font-size: 60px; line-height: 70px;
    color: var(--green); letter-spacing: 1px;
  }
  .ad-slot { position: absolute; left: 1070px; top: 28px; width: 111px; height: 75px; background: var(--ad-grey); }
  .banner {
    position: absolute; left: 0; top: 109px; width: 1200px; height: 46px; background: var(--green);
  }
  .banner-title {
    position: absolute; left: 0; top: 0; width: 100%; text-align: center;
    font-family: "Carlito", Calibri, sans-serif; font-size: 39px; line-height: 46px; color: #000;
  }
  .web { position: absolute; top: 27px; font-size: 12.5px; color: var(--paper); }
  .web.left { left: 14px; }
  .web.right { right: 14px; }
  .story { position: absolute; top: 166px; }
  .story h2 {
    font-family: "Tinos", "Times New Roman", serif; font-weight: normal;
    font-size: 25px; line-height: 31px;
  }
  .story p { font-size: 14px; line-height: 20.5px; }
  .photo { display: block; }
  .garlic { left: 15px; width: 375px; }
  .garlic .photo {
    float: left; width: 111px; height: 107px; margin: 1px 16px 0 0;
    background: radial-gradient(circle at 45% 45%, #f3eee2, #d9ccb0 70%, #b7a88a);
  }
  .chickpeas { left: 405px; width: 400px; }
  .chickpeas .spacer { float: right; width: 0; height: 91px; }
  .chickpeas .photo {
    float: right; clear: right; width: 112px; height: 107px; margin: 2px 0 4px 6px;
    border: 1px solid var(--frame);
    background: radial-gradient(ellipse at 50% 52%, #e3c48a 0, #d6b06c 32%, #f4f1ea 40%, #ffffff 60%);
  }
  .ginger { left: 836px; width: 346px; }
  .ginger .photo {
    float: right; width: 111px; height: 105px; margin: 2px 0 4px 6px;
    border: 1px solid var(--frame);
    background: radial-gradient(ellipse at 50% 50%, #e8c88a 0, #c9a064 40%, #ffffff 65%);
  }
</style>
</head>
<body>
<div class="page">
  <div class="top-rule"></div>
  <div class="dateline">
    <div>Sunday</div>
    <div>10 January 2016</div>
    <div class="city">New York</div>
  </div>
  <h1 class="masthead">Tidal Crumbs</h1>
  <div class="ad-slot"></div>

  <div class="banner">
    <div class="banner-title">Lorem Ipsum dolor sit amet</div>
    <div class="web left">www.tidalcrumbs-eats.com</div>
    <div class="web right">www.tidalcrumbs-eats.com</div>
  </div>

  <article class="story garlic">
    <div class="photo" role="img" aria-label="Photo of garlic bulbs"></div>
    <h2>Garlic is high in Minerals &amp; Vitamins</h2>
    <p>Lorem Ipsum dolor sit amet, consectetuer adipiscing elit. Duis tellus. Donec ante dolor, iaculis nec, gravida ac, cursus in, eros. Mauris vestibulum, felis et egestas ullamcorper, purus nibh vehicula sem, eu egestas ante nisl non justo. Fusce tincidunt, lorem nev dapibus consectetuer, leo orci mollis ipsum, eget suscipit eros purus in ante.</p>
  </article>

  <article class="story chickpeas">
    <h2>Chickpeas are high on fiber</h2>
    <div class="spacer"></div>
    <div class="photo" role="img" aria-label="Photo of a plate of chickpeas"></div>
    <p>Lorem Ipsum dolor sit amet, consectetuer adipiscing elit. Duis tellus. Donec ante dolor, iaculis nec, gravida ac, cursus in, eros. Mauris vestibulum, felis et egestas ullamcorper, purus nibh vehicula sem, eu egestas ante nisl non justo. Fusce tincidunt, lorem nev dapibus consectetuer, leo orci mollis ipsum, eget suscipit eros purus in ante.</p>
    <p>Lorem Ipsum dolor sit amet, consectetuer adipiscing elit. Duis tellus. Donec .</p>
  </article>

  <article class="story ginger">
    <h2>Ginger contains Gingerol, a substance with powerful medicinal properties</h2>
    <div class="photo" role="img" aria-label="Photo of ginger root"></div>
    <p>Lorem Ipsum dolor sit amet, consectetuer adipiscing elit. Duis tellus. Donec ante dolor, iaculis nec, gravi da ac, cursus in, eros. Mauris vestibulum, felis et egestas ullamcorper, purus nibh vehicul a se m, eu egestas ante. consectet uer adipiscing elit.</p>
  </article>
</div>
</body>
</html>
```